Modern Billboard Ad for Criminal Defense Firm

10.5 x 36 We're looking for something to set us apart from the local competition. Looking for sleek and modern. We're a mid-sized firm in a small market city. We want to give the artist room to be creative on this one.
Thanks

Target Market(s)

Adult clients who have been charged with a crime/DWI

Industry/Entity Type

legal

Font styles to use
Serif
Sans Serif

Requirements
Must have
• Needs to have the firm name in large lettering. Law Offices of Marcus T Whitfield. “PLLC” does not have to be included. Phone number of (555) 384-1927 should be included but not the main focus.
Nice to have
• A call to action or something similar. “Don’t go it alone, call today.”, “ Arrested?”

```html
<!DOCTYPE html>
<html lang="en">
<head>
<meta charset="utf-8">
<title>Billboard – Law Offices of Marcus T Whitfield</title>
<link rel="stylesheet" href="https://fonts.googleapis.com/css2?family=Archivo:wdth,wght@112..125,500..800&display=swap">
<style>
  :root {
    --paper: #ffffff;
    --board-light: #dedede;
    --board-mid: #c9c9c9;
    --ink: #2a2a2a;
    --band: #2b2b2b;
    --white: #ffffff;
    --accent: #c1272d;
    --badge-blue: #2aa9e0;
    --photo-dark: #3a3a3a;
    --photo-light: #9a9a9a;
  }
  * { margin: 0; padding: 0; box-sizing: border-box; }
  html, body {
    width: 1055px; height: 1200px; overflow: hidden;
    background: var(--paper);
  }
  .billboard {
    position: absolute; left: 40px; top: 456px;
    width: 975px; height: 287px;
    background: var(--board-light);
    overflow: hidden;
    font-family: "Archivo", "Helvetica Neue", Arial, sans-serif;
    font-stretch: 125%;
    color: var(--ink);
  }
  .backdrop-photo {
    position: absolute; inset: 0;
    background: radial-gradient(ellipse at 45% 55%, var(--board-mid) 0%, var(--board-light) 65%);
  }
  .edge-column {
    position: absolute; right: 0; top: 0;
    width: 57px; height: 100%;
    background: var(--band);
  }
  .name-band {
    position: absolute; left: 0; top: 97px;
    width: 760px; height: 94px;
    background: var(--band);
  }
  .award-badge {
    position: absolute; left: 32px; top: 20px;
    width: 110px; height: 159px;
    background: var(--badge-blue);
  }
  .firm-lead {
    position: absolute; left: 168px; top: 34px;
    font-size: 40px; font-weight: 600; letter-spacing: -0.5px;
    line-height: 1;
  }
  .firm-name {
    position: absolute; left: 168px; top: 120px;
    font-size: 43px; font-weight: 700; letter-spacing: -0.8px;
    line-height: 1; color: var(--white);
    white-space: nowrap;
  }
  .contact {
    position: absolute; left: 32px; top: 202px;
    font-size: 22px; font-weight: 600; line-height: 1.08;
    white-space: nowrap;
  }
  .cta-pill {
    position: absolute; left: 480px; top: 209px;
    width: 209px; height: 50px;
    border-radius: 25px;
    background: var(--accent);
    color: var(--white);
    font-size: 28px; font-weight: 600;
    display: flex; align-items: center; justify-content: center;
  }
  .attorney-portrait {
    position: absolute; left: 719px; top: 29px;
    width: 229px; height: 229px;
    background: linear-gradient(135deg, var(--photo-dark) 0%, var(--photo-light) 55%, var(--photo-dark) 100%);
  }
</style>
</head>
<body>
  <section class="billboard">
    <div class="backdrop-photo" role="img" aria-label="Faded photograph of handcuffed hands behind the text"></div>
    <div class="edge-column"></div>
    <div class="name-band"></div>
    <div class="award-badge" role="img" aria-label="Community choice award badge"></div>
    <p class="firm-lead">Law Offices of</p>
    <h1 class="firm-name">Marcus T Whitfield</h1>
    <p class="contact">Don’t go it alone, call today.<br>(555) 384-1927</p>
    <div class="cta-pill">Arrested?</div>
    <div class="attorney-portrait" role="img" aria-label="Black and white portrait of the attorney in a suit vest, jacket over shoulder"></div>
  </section>
</body>
</html>
```